KOVA WIRING PTE LTD
KOVA WIRING NAME CARD
Project: KOVA WIRING PTE LTD
KOVA WIRING PTE LTD - Engineering
Creative Brief
Professional
Deren Whitcombe
Manager
57 Tannery Lane #03-22 Silverbrook Industrial Complex Singapore 347912
derenkovawiring@mailbox-example.net
Reg No. 198733502K
https://www.filevault-example.net/share/7qe2kx9/ZTRmPwq4HnLc?dl=0 Pleas find folder for the logo design A.I. file. Thanks Client love the 3 colour in the logo design for FengShui purposes.
harlowbek harlowbek
Hi my client like your design #218, Can you give the stationary set for #218. We try to finalize by tomorrow. Thanks

```html
<!DOCTYPE html>
<html lang="en">
<head>
<meta charset="utf-8">
<title>Kova Wiring – Business Card</title>
<link href="https://fonts.googleapis.com/css2?family=Open+Sans:wght@400;600&display=swap" rel="stylesheet">
<style>
  :root {
    --bg-light: #e9e9e9;
    --bg-dark: #c9c9c9;
    --card: #ffffff;
    --ink: #2b2b2b;
    --muted: #555555;
    --green: #1f8a3c;
    --shadow: rgba(0,0,0,0.22);
  }
  * { margin: 0; padding: 0; box-sizing: border-box; }
  html, body { width: 1200px; height: 902px; overflow: hidden; }
  body {
    background: radial-gradient(ellipse at 50% 40%, var(--bg-light), var(--bg-dark));
    font-family: "Open Sans", Arial, sans-serif;
    color: var(--ink);
    position: relative;
  }
  .card {
    position: absolute;
    width: 640px;
    height: 366px;
    background: var(--card);
    box-shadow: 0 10px 28px var(--shadow);
  }
  .card--back { left: 280px; top: 62px; }
  .card--front { left: 280px; top: 474px; }

  .contact {
    position: absolute;
    right: 44px;
    top: 40px;
    text-align: right;
    font-size: 13px;
    line-height: 1.65;
    color: var(--muted);
  }
  .contact__row { display: flex; justify-content: flex-end; align-items: center; gap: 7px; }
  .contact__icon { width: 9px; height: 9px; fill: var(--ink); }
  .website {
    position: absolute;
    left: 44px;
    bottom: 40px;
    font-size: 15px;
    letter-spacing: 2px;
    color: var(--ink);
  }
  .website strong { font-weight: 600; }

  .brand {
    position: absolute;
    left: 44px;
    bottom: 44px;
    display: flex;
    align-items: center;
    gap: 12px;
  }
  .brand__mark { width: 52px; height: 52px; background: var(--green); }
  .brand__name {
    font-size: 30px;
    font-weight: 600;
    letter-spacing: 3px;
    color: var(--ink);
  }
  .person {
    position: absolute;
    right: 44px;
    top: 150px;
    text-align: right;
  }
  .person__name { font-size: 17px; font-weight: 600; color: var(--green); }
  .person__role { font-size: 14px; color: var(--muted); margin-top: 2px; }
</style>
</head>
<body>
  <section class="card card--back">
    <div class="contact">
      <div class="contact__row">57 Tannery Lane #03-22</div>
      <div class="contact__row">Singapore 347912 <svg class="contact__icon" viewBox="0 0 10 10"><path d="M5 0a3.5 3.5 0 0 0-3.5 3.5C1.5 6 5 10 5 10s3.5-4 3.5-6.5A3.5 3.5 0 0 0 5 0z"/></svg></div>
      <div class="contact__row">6555 0142 <svg class="contact__icon" viewBox="0 0 10 10"><path d="M2 0l2 2.5-1 1.2a6 6 0 0 0 3.3 3.3l1.2-1L10 8l-1.2 2C4 10 0 6 0 1.2z"/></svg></div>
      <div class="contact__row">derenkovawiring@mailbox-example.net <svg class="contact__icon" viewBox="0 0 10 10"><rect x="0" y="1.5" width="10" height="7"/></svg></div>
    </div>
    <div class="website">www.<strong>kovawiring-example</strong>.net</div>
  </section>

  <section class="card card--front">
    <div class="brand">
      <div class="brand__mark"></div>
      <div class="brand__name">KOVA WIRING</div>
    </div>
    <div class="person">
      <div class="person__name">Deren Whitcombe</div>
      <div class="person__role">Owner</div>
    </div>
  </section>
</body>
</html>
```